Brightwell electrical flyer for distribution to get more clients

I need to make a flyer to distribute to the local neighbourhood. we are an electrical company and the name is Brightwell electrical contractors. the website is www.brightwell-electric-demo.ca We do custom homes, knob and tube home re-wires, fuse to breaker panel upgrades, service upgrades 100 amp and 200 amp, pot lights, roof de-icing cables, floor heat cables, pot lights, surge protection, smoke detectors. Flyer size is half page 216mm X 139mm

Target Market(s)

home owners

Industry/Entity Type

Electrician

Font styles to use
Sans Serif

Requirements
Must have
• flyer must list our services and geared more toward the knob and tube replacement. must have company name and number 416-555-0148 and our OPL/RCMA licence number which is 4829306
Nice to have
• try to match the colour scheme of the website with the flyer www.brightwell-electric-demo.ca

```html
<!DOCTYPE html>
<html lang="en">
<head>
<meta charset="utf-8">
<title>Brightwell Electrical Contractors – Flyer</title>
<link href="https://fonts.googleapis.com/css2?family=Open+Sans:wght@700;800&family=Source+Sans+3:wght@300;400;600;700&display=swap" rel="stylesheet">
<style>
  :root{
    --charcoal:#333333;
    --charcoal-deep:#2b2b2b;
    --yellow:#fcc918;
    --gold:#c9a21d;
    --gold-text:#ffe46e;
    --orange:#ef8a22;
    --white:#ffffff;
    --muted:#8d8d8d;
    --stage:#eeeeee;
  }
  *{box-sizing:border-box;margin:0;padding:0}
  html,body{width:1036px;height:1200px;overflow:hidden;background:var(--stage)}
  body{position:relative;font-family:"Source Sans 3",sans-serif;color:var(--white)}

  .flyer{position:absolute;left:78px;width:880px;height:566px;overflow:hidden;background:var(--charcoal);box-shadow:0 6px 18px rgba(0,0,0,.25)}
  .flyer--front{top:22px}
  .flyer--back{top:612px}
  .flyer svg.shapes{position:absolute;inset:0;width:100%;height:100%}
  .abs{position:absolute}

  .brand{color:var(--yellow);font-weight:700;line-height:1;white-space:nowrap}
  .brand__name{display:block;text-transform:uppercase}
  .brand__sub{display:block}
  .flyer--front .brand{right:20px;top:104px;text-align:center;width:300px}
  .flyer--front .brand__name{font-size:44px;letter-spacing:3px}
  .flyer--front .brand__sub{font-size:19px;letter-spacing:1.5px;margin-top:8px}

  .intro{right:20px;top:262px;width:225px;text-align:right;font-size:12px;line-height:1.38;color:#f1f1f1}
  .intro p + p{margin-top:14px}

  .front-contact{left:34px;top:488px;color:var(--charcoal-deep)}
  .front-contact__phone{font-family:"Open Sans",sans-serif;font-weight:800;font-size:42px;letter-spacing:-0.5px;line-height:1}
  .front-contact__web{font-family:"Open Sans",sans-serif;font-weight:700;font-size:15px;letter-spacing:1px;margin-top:8px;white-space:nowrap}

  .licence{display:flex;align-items:center;gap:10px}
  .licence__mark{width:64px;height:64px;border-radius:50%;background:var(--orange);flex:none}
  .licence__number{font-size:13px;color:var(--muted);letter-spacing:.3px;white-space:nowrap}
  .flyer--front .licence{right:20px;top:452px;flex-direction:column;align-items:flex-end;gap:6px}
  .flyer--front .licence__mark{width:56px;height:56px}

  .flyer--back .brand{left:22px;top:60px;width:270px;text-align:center}
  .flyer--back .brand__name{font-size:36px;letter-spacing:3px}
  .flyer--back .brand__sub{font-size:16px;letter-spacing:1.2px;margin-top:6px}

  .call{right:22px;top:26px;text-align:right}
  .call__label{font-weight:700;font-size:20px;letter-spacing:.2px}
  .call__phone{font-family:"Open Sans",sans-serif;font-weight:800;font-size:46px;line-height:1.1}

  .ribbon{left:0;top:160px;width:570px;height:40px;background:var(--gold);border-radius:0 20px 20px 0;padding-left:28px;font-weight:700;font-size:24px;line-height:40px;color:var(--gold-text);text-transform:uppercase;letter-spacing:-.2px}

  .services{left:30px;top:218px;display:grid;grid-template-columns:237px 311px 280px;row-gap:16px;list-style:none}
  .service{display:flex;align-items:center;gap:9px;font-weight:300;font-size:25px;line-height:26px;white-space:nowrap}
  .service svg{width:22px;height:22px;flex:none}

  .flyer--back .licence{left:32px;top:376px}

  .photo{border-radius:50%;border:5px solid var(--white);box-shadow:0 3px 8px rgba(0,0,0,.35)}
  .photo--detector{left:409px;top:386px;width:114px;height:114px;background:radial-gradient(circle at 45% 45%,#ffffff,#d9d9d9 60%,#9a9a9a)}
  .photo--cables{left:551px;top:377px;width:128px;height:128px;background:radial-gradient(circle,#a9714c,#6d4027)}
  .photo--roof{left:710px;top:350px;width:140px;height:140px;background:linear-gradient(160deg,#e9eef2,#b9c3ca 55%,#4c3d34)}

  .contacts{left:28px;right:22px;top:522px;display:flex;justify-content:space-between;align-items:center;font-size:20px;font-weight:400;color:var(--charcoal-deep);white-space:nowrap}
  .contact{display:flex;align-items:center;gap:8px}
  .contact svg{width:20px;height:20px;flex:none}
</style>
</head>
<body>

<section class="flyer flyer--front" aria-label="Flyer front">
  <svg class="shapes" viewBox="0 0 880 566" preserveAspectRatio="none">
    <defs>
      <linearGradient id="interiorTones" x1="0" y1="0" x2="1" y2="1">
        <stop offset="0" stop-color="#e9ecef"/>
        <stop offset=".55" stop-color="#cfcac4"/>
        <stop offset="1" stop-color="#9a6b45"/>
      </linearGradient>
    </defs>
    <rect width="880" height="566" fill="url(#interiorTones)" role="img" aria-label="Photo of a bright modern kitchen with bar stools and wood floor"/>
    <polygon points="0,408 52,408 0,450" fill="var(--charcoal)"/>
    <polygon points="0,448 345,448 403,566 0,566" fill="var(--charcoal)"/>
    <polygon points="0,448 337,448 393,566 0,566" fill="var(--yellow)"/>
    <polygon points="436,0 880,0 880,566 682,566 458,146 436,0" fill="var(--white)"/>
    <polygon points="450,0 880,0 880,566 686,566 460,140" fill="var(--yellow)"/>
    <polygon points="450,0 880,0 880,566 746,566 496,140 465,0" fill="var(--charcoal)"/>
    <polygon points="458,142 496,140 746,566 686,566" fill="var(--yellow)"/>
  </svg>

  <div class="brand abs">
    <span class="brand__name">Brightwell</span>
    <span class="brand__sub">Electrical Contractors Inc.</span>
  </div>

  <div class="intro abs">
    <p>We are licenced electrical contractors based out of Toronto and serving all of the GTA. We specialize in custom homes and knob and tube removal. We are fully licenced and insured.</p>
    <p>We offer a wide variety of services. From custom homes to home re-wires and renovations we can do it all.</p>
  </div>

  <div class="licence abs">
    <span class="licence__mark" aria-hidden="true"></span>
    <span class="licence__number">OPL/RCMA 4829306</span>
  </div>

  <div class="front-contact abs">
    <div class="front-contact__phone">416-555-0148</div>
    <div class="front-contact__web">www.brightwell-electric-demo.ca</div>
  </div>
</section>

<section class="flyer flyer--back" aria-label="Flyer back">
  <svg class="shapes" viewBox="0 0 880 566" preserveAspectRatio="none">
    <polygon points="0,486 880,398 880,566 0,566" fill="var(--white)"/>
    <polygon points="0,494 880,406 880,566 0,566" fill="var(--yellow)"/>
  </svg>

  <div class="brand abs">
    <span class="brand__name">Brightwell</span>
    <span class="brand__sub">Electrical Contractors Inc.</span>
  </div>

  <div class="call abs">
    <div class="call__label">CALL US TODAY</div>
    <div class="call__phone">416-555-0148</div>
  </div>

  <div class="ribbon abs">We offer a wide variety of services</div>

  <ul class="services abs">
    <li class="service"><svg viewBox="0 0 22 22"><circle cx="11" cy="11" r="11" fill="var(--yellow)"/><path d="M9 6l5 5-5 5" fill="none" stroke="var(--charcoal)" stroke-width="2.6" stroke-linecap="round" stroke-linejoin="round"/></svg>Custom homes</li>
    <li class="service"><svg viewBox="0 0 22 22"><circle cx="11" cy="11" r="11" fill="var(--yellow)"/><path d="M9 6l5 5-5 5" fill="none" stroke="var(--charcoal)" stroke-width="2.6" stroke-linecap="round" stroke-linejoin="round"/></svg>Pot lights</li>
    <li class="service"><svg viewBox="0 0 22 22"><circle cx="11" cy="11" r="11" fill="var(--yellow)"/><path d="M9 6l5 5-5 5" fill="none" stroke="var(--charcoal)" stroke-width="2.6" stroke-linecap="round" stroke-linejoin="round"/></svg>Service upgrade</li>
    <li class="service"><svg viewBox="0 0 22 22"><circle cx="11" cy="11" r="11" fill="var(--yellow)"/><path d="M9 6l5 5-5 5" fill="none" stroke="var(--charcoal)" stroke-width="2.6" stroke-linecap="round" stroke-linejoin="round"/></svg>Surge protection</li>
    <li class="service"><svg viewBox="0 0 22 22"><circle cx="11" cy="11" r="11" fill="var(--yellow)"/><path d="M9 6l5 5-5 5" fill="none" stroke="var(--charcoal)" stroke-width="2.6" stroke-linecap="round" stroke-linejoin="round"/></svg>Knob and tube re-wiring</li>
    <li class="service"><svg viewBox="0 0 22 22"><circle cx="11" cy="11" r="11" fill="var(--yellow)"/><path d="M9 6l5 5-5 5" fill="none" stroke="var(--charcoal)" stroke-width="2.6" stroke-linecap="round" stroke-linejoin="round"/></svg>Smoke detectors</li>
    <li class="service"><svg viewBox="0 0 22 22"><circle cx="11" cy="11" r="11" fill="var(--yellow)"/><path d="M9 6l5 5-5 5" fill="none" stroke="var(--charcoal)" stroke-width="2.6" stroke-linecap="round" stroke-linejoin="round"/></svg>Electrical solutions</li>
    <li class="service"><svg viewBox="0 0 22 22"><circle cx="11" cy="11" r="11" fill="var(--yellow)"/><path d="M9 6l5 5-5 5" fill="none" stroke="var(--charcoal)" stroke-width="2.6" stroke-linecap="round" stroke-linejoin="round"/></svg>Fuse to breaker upgrade</li>
    <li class="service"><svg viewBox="0 0 22 22"><circle cx="11" cy="11" r="11" fill="var(--yellow)"/><path d="M9 6l5 5-5 5" fill="none" stroke="var(--charcoal)" stroke-width="2.6" stroke-linecap="round" stroke-linejoin="round"/></svg>Roof and floor heating</li>
  </ul>

  <div class="licence abs">
    <span class="licence__mark" aria-hidden="true"></span>
    <span class="licence__number">OPL/RCMA 4829306</span>
  </div>

  <div class="photo photo--detector abs" role="img" aria-label="Photo of a white ceiling smoke detector"></div>
  <div class="photo photo--cables abs" role="img" aria-label="Photo of old knob and tube wiring between wood joists"></div>
  <div class="photo photo--roof abs" role="img" aria-label="Photo of de-icing cables on a snowy roof"></div>

  <div class="contacts abs">
    <span class="contact"><svg viewBox="0 0 22 22"><circle cx="11" cy="11" r="9.5" fill="none" stroke="var(--charcoal-deep)" stroke-width="1.8"/><circle cx="11" cy="11" r="3.5" fill="none" stroke="var(--charcoal-deep)" stroke-width="1.8"/></svg>hello@brightwell-electric-demo.ca</span>
    <span class="contact"><svg viewBox="0 0 22 22"><circle cx="11" cy="11" r="9.5" fill="none" stroke="var(--charcoal-deep)" stroke-width="1.8"/><path d="M7.5 6.5c-.6 3.6 3.6 8.4 8 8l.6-2-2.4-1.2-1 1c-1.4-.6-2.4-1.6-3-3l1-1L9.5 6z" fill="var(--charcoal-deep)"/></svg>416-555-0148</span>
    <span class="contact"><svg viewBox="0 0 22 22"><circle cx="11" cy="11" r="9.5" fill="none" stroke="var(--charcoal-deep)" stroke-width="1.8"/><rect x="10" y="9.5" width="2" height="7" fill="var(--charcoal-deep)"/><circle cx="11" cy="6.5" r="1.3" fill="var(--charcoal-deep)"/></svg>www.brightwell-electric-demo.ca</span>
  </div>
</section>

</body>
</html>
```